Birchway Lending Social Media Campaign

I need social media campaign banners. Facebook and Instagram.
I would like them to incorporate local photos, my photo and my logo. I have some sample files of previous campaigns and I have a color scheme associated with my brand. My business operates in St. John's Newfoundland.

Target Market(s)

Home Buyers, Home Owners

Industry/Entity Type

Mortgage Brokering

Logo Text

Birchway Lending

Logo styles of interest
Lettermark Logo
Font styles to use
Other font styles liked:
• Times New Roman, I'm open to suggestion

Colors
0054AA
0677BA
7BADD7
CADEEF
E8F1F8
EE7325
F08F49
F5BC92
FAE3D3
FDF4ED

Requirements
Must have
• My name, photo, contact info, slogan
Nice to have
• We can discuss slogans to use, I can provide some suggestions.

```html
<!DOCTYPE html>
<html lang="en">
<head>
<meta charset="utf-8">
<title>Birchway Lending – Find the Key to Your Home</title>
<link href="https://fonts.googleapis.com/css2?family=Montserrat:wght@300;400;500;600;700;800&display=swap" rel="stylesheet">
<style>
  :root {
    --navy-deep: #08185a;
    --navy: #0d2470;
    --navy-soft: #1b3484;
    --orange: #ff4a12;
    --white: #ffffff;
    --sky: #d9dbe0;
    --stone: #a59c98;
    --house-red: #a8443c;
    --house-blue: #4a6690;
  }
  * { margin: 0; padding: 0; box-sizing: border-box; }
  html, body {
    width: 1200px; height: 675px; overflow: hidden;
    background: var(--navy-deep);
  }
  .banner {
    position: relative; width: 1200px; height: 675px; overflow: hidden;
    font-family: "Montserrat", sans-serif; color: var(--white);
    background: linear-gradient(90deg, var(--navy-deep) 0%, var(--navy) 45%, var(--navy-soft) 100%);
  }
  .city-photo {
    position: absolute; left: 380px; top: 0; width: 820px; height: 675px;
    background: linear-gradient(180deg,
      var(--sky) 0%, var(--sky) 22%,
      var(--stone) 32%,
      var(--house-red) 48%,
      var(--house-blue) 60%,
      #6b6f88 70%,
      var(--navy-soft) 86%,
      var(--navy) 100%);
    -webkit-mask-image: linear-gradient(90deg, transparent 0%, rgba(0,0,0,.5) 20%, #000 45%);
            mask-image: linear-gradient(90deg, transparent 0%, rgba(0,0,0,.5) 20%, #000 45%);
    opacity: .9;
  }
  .brand {
    position: absolute; left: 36px; top: 34px;
    display: flex; align-items: center; gap: 10px;
  }
  .brand-mark { width: 22px; height: 22px; background: var(--white); }
  .brand-name { font-weight: 700; font-size: 18px; letter-spacing: .5px; text-transform: uppercase; }
  .headline {
    position: absolute; left: 34px; top: 316px;
    font-size: 68px; line-height: 62px; font-weight: 300; letter-spacing: -1px;
    text-transform: uppercase;
  }
  .headline strong { color: var(--orange); font-weight: 800; }
  .subline {
    position: absolute; left: 38px; top: 458px;
    font-size: 19px; line-height: 27px; font-weight: 500;
  }
  .subline strong { color: var(--orange); font-weight: 800; font-size: 22px; text-transform: uppercase; }
  .contact { position: absolute; top: 608px; display: flex; align-items: center; gap: 8px; }
  .contact-phone { left: 38px; }
  .contact-web { left: 302px; }
  .contact-label { font-size: 15px; font-weight: 500; line-height: 18px; }
  .contact-number { font-size: 25px; font-weight: 800; line-height: 30px; }
  .contact-heading { font-size: 23px; font-weight: 800; line-height: 26px; text-transform: uppercase; }
  .contact-url { font-size: 14px; font-weight: 500; line-height: 18px; }
  .advisor-photo {
    position: absolute; left: 866px; top: 272px; width: 312px; height: 403px;
    border-radius: 140px 140px 0 0;
    background: linear-gradient(180deg, #c9a27a 0%, #b88e66 35%, #3a3f58 62%, #1e2642 100%);
  }
  .cta {
    position: absolute; left: 911px; top: 611px; width: 229px; height: 40px;
    background: var(--white); border-radius: 6px;
    display: flex; align-items: center; justify-content: center;
    color: var(--orange); font-weight: 800; font-size: 19px; text-transform: uppercase;
  }
</style>
</head>
<body>
<main class="banner">
  <div class="city-photo" role="img" aria-label="St. John's hillside with cathedral towers and colourful row houses"></div>

  <div class="brand">
    <span class="brand-mark"></span>
    <span class="brand-name">Birchway Lending</span>
  </div>

  <h1 class="headline">Find the <strong>Key</strong><br>To Your <strong>Home</strong></h1>

  <p class="subline">Let Us Help You Unlock Your <strong>Dream Home Today</strong><br>With Low Rates &amp; Great Deals!</p>

  <div class="contact contact-phone">
    <svg width="26" height="40" viewBox="0 0 26 40" aria-hidden="true">
      <rect x="1" y="1" width="24" height="38" rx="4" fill="#ff4a12"/>
      <path d="M8 11c1-1 2-1 3 0l2 3c.5 1 0 2-1 2.5 1 3 2.5 5 5 6.5.5-1 1.5-1.5 2.5-1l2 2c1 1 .5 2-.5 3-3 2-7-1-10-5s-4-8-3-11z" fill="#fff"/>
    </svg>
    <div>
      <div class="contact-label">Call Maren at :</div>
      <div class="contact-number">709 555 0142</div>
    </div>
  </div>

  <div class="contact contact-web">
    <svg width="38" height="38" viewBox="0 0 38 38" aria-hidden="true">
      <g fill="none" stroke="#ff4a12" stroke-width="3">
        <circle cx="19" cy="19" r="16"/>
        <ellipse cx="19" cy="19" rx="7" ry="16"/>
        <line x1="3" y1="19" x2="35" y2="19"/>
        <line x1="6" y1="11" x2="32" y2="11"/>
        <line x1="6" y1="27" x2="32" y2="27"/>
      </g>
    </svg>
    <div>
      <div class="contact-heading">Website :</div>
      <div class="contact-url">www.birchwaylending.com</div>
    </div>
  </div>

  <div class="advisor-photo" role="img" aria-label="Portrait of mortgage advisor Maren"></div>

  <div class="cta">Get Started</div>
</main>
</body>
</html>
```